Website for a company offering full serivce charging solutions for electric cars

The company "vorn-werk" (english: "front-works") offering all-in-one-solutions for charging infrastructure for electric mobility.

There are four products:
1- Wallboxes for single-family homes
2- Solutions for property devloper/-management for property parking space
3- All-in-one-charging solution for municipalities/communities
4- Solutions for tourism/hotels/holiday appartments

The Website structure:
1. Main Page
2.1. Product Page Single Homes
2.2. Product Page Property Management / Parking
2.3. Product Page Municipality
2.4. Product Page Tourism
3. Contact Form / Request for information
4. Imprint / Legal

The Website should be built on Wordpress with a powerful possibility to simply add/modify specific landing pages.

We would like you to implement the website later and also maintain it if possible, but we would be able to do minor modifications by ourselfs (for A/B-Testing)

The website should be clear and simple, easy to understand.
Target group is mainly B2C without deeper knowledge of that topic.

It should suggest, that we will provide a very simple way to get the charging infrastructure done.

We need a contact form, maybe we will use Leadmill later.

Attached you will find a draft of the main page and a landing page (for 2.2) - it is just the content, please ignore the design. We would love to let you create a suitable design.
Also you will find some drafts a bit different for the same story.

I added also a few stock photos, but they don't need to be used! If you have better ideas, you are welcome!

Charging/Electric mobility

Sans Serif

• Based on Wordpress, and the designer should be able to implement it on Wordpress on a later step

```html
<!DOCTYPE html>
<html lang="en">
<head>
<meta charset="utf-8">
<title>vorn-werk – Charging Solutions</title>
<link href="https://fonts.googleapis.com/css2?family=Krona+One&family=Michroma&family=Poppins:wght@400;500;600;700&display=swap" rel="stylesheet">
<style>
:root{
  --navy:#1a1d2e;
  --navy-2:#23283d;
  --pink:#e0259c;
  --purple:#7b4fd6;
  --violet:#9a3fc4;
  --white:#ffffff;
  --ink:#1b1b1f;
  --grad:linear-gradient(90deg,#e0259c,#7b4fd6);
}
*{margin:0;padding:0;box-sizing:border-box}
html,body{width:1200px;height:4874px;overflow:hidden}
body{position:relative;background:var(--white);font-family:"Poppins",sans-serif;color:var(--ink)}
.abs{position:absolute}
.heading{font-family:"Krona One",sans-serif;font-weight:400;text-align:center;letter-spacing:1px}
.btn{position:absolute;display:flex;align-items:center;justify-content:center;border-radius:30px;background:var(--grad);color:var(--white);font-family:"Krona One",sans-serif;font-size:18px;letter-spacing:1px;border:2px solid var(--white)}
/* header */
.site-header{left:0;top:0;width:1200px;height:133px;background:var(--navy)}
.brand{display:flex;align-items:center;gap:10px;color:var(--white);font-family:"Poppins",sans-serif;font-weight:500;font-size:32px}
.brand-dot{width:18px;height:18px;border-radius:50%;background:var(--pink)}
.header-phone{left:748px;top:34px;color:var(--pink);font-weight:700;font-size:22px}
.main-nav{left:452px;top:88px;display:flex;gap:24px;font-size:17px;color:var(--white);font-weight:500}
.main-nav .active{color:var(--pink)}
/* hero */
.hero{left:0;top:133px;width:1200px;height:722px;background:linear-gradient(120deg,#2d3a5c 0%,#1f2942 45%,#3a4866 70%,#151b2c 100%)}
.hero-title{left:0;top:255px;width:1200px;text-align:center;font-family:"Michroma",sans-serif;font-size:64px;line-height:74px;color:var(--white)}
.hero-sub{left:200px;top:438px;width:800px;text-align:center;font-size:22px;line-height:28px;color:var(--white)}
/* about */
.about-title{left:0;top:940px;width:1200px;font-size:50px}
.about-text{left:205px;top:1036px;width:790px;text-align:center;font-size:19.5px;line-height:28.5px}
.about-text strong{font-weight:600}
/* private */
.private-title{left:0;top:1560px;width:1200px;font-size:50px;line-height:74px;color:var(--white)}
.feature{position:absolute;display:flex;align-items:flex-start;gap:30px;width:420px;color:var(--white);font-size:18.5px;line-height:24px}
.feature-icon{flex:none;width:92px;height:92px;border-radius:50%;background:var(--white);display:flex;align-items:center;justify-content:center;margin-top:-14px}
.feature-icon svg{width:52px;height:52px}
/* municipality */
.muni-title{left:0;top:2585px;width:1200px;font-size:50px}
.bracket{left:167px;top:2732px;width:151px;height:520px;background:var(--violet)}
.photo{left:190px;top:2752px;width:400px;height:470px;background:linear-gradient(160deg,#8a8f98 0%,#3f444c 40%,#1e2126 70%,#5b3b2c 100%)}
.check-list{list-style:none}
.check-list li{position:absolute;display:flex;gap:20px}
.check-list svg{flex:none;width:22px;height:20px;margin-top:2px}
.muni-list li{left:630px;width:420px;font-size:15px;line-height:22px}
/* business */
.biz-title{left:0;top:3430px;width:1200px;font-size:50px;line-height:74px;color:var(--white)}
.biz-list li{width:400px;font-size:19px;line-height:27px;color:var(--white)}
.biz-sub{list-style:none;margin-top:8px}
.biz-sub li{position:static;display:block;font-size:15px;line-height:31px;padding-left:26px;position:relative}
.biz-sub li::before{content:"";position:absolute;left:0;top:12px;width:9px;height:9px;border-radius:50%;background:var(--white)}
/* footer */
.footer-bg{left:0;top:4430px;width:1200px;height:444px;background:var(--navy)}
.footer-head{font-family:"Krona One",sans-serif;font-size:36px;color:var(--white)}
.footer-links{left:568px;top:4548px;list-style:none;font-size:18px;line-height:37px;color:var(--white)}
.contact-item{position:absolute;left:790px;display:flex;gap:22px;color:var(--white);font-size:18px;line-height:27px;width:330px}
.contact-icon{flex:none;width:36px;height:36px;border-radius:50%;background:var(--violet);display:flex;align-items:center;justify-content:center}
.social{position:absolute;top:4664px;width:52px;height:52px;border-radius:50%;background:var(--violet)}
.footer-rule{left:0;top:4790px;width:1200px;height:1px;background:#3a3f55}
.copyright{left:0;top:4822px;width:1200px;text-align:center;font-size:14px;color:var(--white)}
</style>
</head>
<body>

<!-- Header -->
<header class="abs site-header">
  <div class="abs brand" style="left:170px;top:58px"><span class="brand-dot"></span>vorn-werk.de</div>
  <div class="abs header-phone">CALL US: 7548 555 0142</div>
  <nav class="abs main-nav">
    <span class="active">Home</span><span>Solutions</span><span>Company</span><span>Services</span><span>Career</span><span>Contact</span>
  </nav>
</header>

<!-- Hero -->
<section class="abs hero" role="img" aria-label="Electric car plugged into a charging station"></section>
<svg class="abs" style="left:0;top:640px" width="1200" height="220" viewBox="0 0 1200 220" aria-hidden="true">
  <defs><linearGradient id="waveGrad" x1="0" x2="1"><stop offset="0" stop-color="#c42fb8"/><stop offset="1" stop-color="#7b4fd6"/></linearGradient></defs>
  <path d="M0,120 C250,220 650,190 1200,40 L1200,220 L0,220 Z" fill="url(#waveGrad)"/>
  <path d="M0,145 C260,235 660,205 1200,62 L1200,220 L0,220 Z" fill="#fff"/>
</svg>
<h1 class="abs hero-title">Front-Works Is<br>Your Partner</h1>
<p class="abs hero-sub">when loading is not only supposed to be easy, but also when the implementation is to come from a single source</p>
<div class="btn" style="left:465px;top:535px;width:270px;height:62px;font-size:20px">GET IN TOUCH</div>

<!-- About -->
<h2 class="abs heading about-title">About&nbsp; Front-Works</h2>
<p class="abs about-text">We offer solutions for private customers, business customers and municipalities who want to get a smart charging solution for e-vehicles quickly, fairly and without having to do anything themselves.From advice to installation, commissioning, billing and maintenance, you get everything from a single source with vorn-werk. On request, we also rent out the charging technology and take care of direct billing with the user in the commercial sector. For municipalities we offer the free full service concept and involve the municipalities in the use of the infrastructure.<br><strong>Ask us about the solution tailored to your individual needs:</strong></p>
<div class="btn" style="left:502px;top:1330px;width:196px;height:52px">VIEW MORE</div>

<!-- Private customer -->
<svg class="abs" style="left:0;top:1410px" width="1200" height="1090" viewBox="0 0 1200 1090" aria-hidden="true">
  <path d="M0,10 C300,80 500,-20 800,30 C1000,60 1100,70 1200,60 L1200,1040 C900,1000 500,1100 0,1060 Z" fill="#1f2438"/>
</svg>
<div class="abs" role="img" aria-label="Electric car at a charging point, darkened backdrop" style="left:700px;top:1450px;width:500px;height:600px;background:radial-gradient(circle at 60% 40%,#3a4560 0%,rgba(31,36,56,0) 65%)"></div>
<h2 class="abs heading private-title">As A Private<br>Customer</h2>

<div class="feature" style="left:173px;top:1772px">
  <span class="feature-icon"><svg viewBox="0 0 52 52"><circle cx="26" cy="24" r="12" fill="none" stroke="#8a3fc8" stroke-width="5" stroke-dasharray="5 3"/><circle cx="26" cy="24" r="5" fill="#e0259c"/><path d="M10,44 H40 l-4,-4 M40,44 l-4,4" stroke="#8a3fc8" stroke-width="3" fill="none"/></svg></span>
  <span>Analysis of the situation with extensive advice on the possibilities of implementation</span>
</div>
<div class="feature" style="left:623px;top:1772px">
  <span class="feature-icon"><svg viewBox="0 0 52 52"><rect x="8" y="24" width="36" height="16" rx="8" fill="#8a3fc8"/><rect x="22" y="8" width="6" height="16" fill="#8a3fc8"/><circle cx="16" cy="32" r="4" fill="#e0259c"/></svg></span>
  <span>Selection of smart wallbox solutions, suitable for your vehicle and your needs</span>
</div>
<div class="feature" style="left:173px;top:1910px">
  <span class="feature-icon"><svg viewBox="0 0 52 52"><circle cx="22" cy="22" r="11" fill="none" stroke="#8a3fc8" stroke-width="6" stroke-dasharray="6 3"/><path d="M28,28 L44,44" stroke="#e0259c" stroke-width="6" stroke-linecap="round"/></svg></span>
  <span>Installation including all necessary materials and activities (breakthroughs, earthworks, etc.)</span>
</div>
<div class="feature" style="left:623px;top:1910px">
  <span class="feature-icon"><svg viewBox="0 0 52 52"><rect x="12" y="8" width="28" height="36" rx="3" fill="none" stroke="#8a3fc8" stroke-width="3"/><path d="M18,18 H34 M18,25 H34 M18,32 H28" stroke="#8a3fc8" stroke-width="3"/><circle cx="38" cy="38" r="7" fill="#e0259c"/></svg></span>
  <span>Annual technical maintenance according to DGUV3 Repair service, taking into account the applicable warranty claims</span>
</div>
<div class="feature" style="left:173px;top:2085px">
  <span class="feature-icon"><svg viewBox="0 0 52 52"><path d="M26,6 L42,12 V26 C42,36 34,43 26,46 C18,43 10,36 10,26 V12 Z" fill="#8a3fc8"/><path d="M18,26 L24,32 L35,20" stroke="#fff" stroke-width="4" fill="none"/></svg></span>
  <span>Checking and acceptance of the registration for available funding opportunities</span>
</div>
<div class="feature" style="left:623px;top:2085px">
  <span class="feature-icon"><svg viewBox="0 0 52 52"><rect x="15" y="6" width="22" height="30" rx="2" fill="none" stroke="#8a3fc8" stroke-width="3"/><path d="M20,14 H32 M20,20 H32 M20,26 H28" stroke="#e0259c" stroke-width="3"/><path d="M6,30 L16,44 H36 L46,30" stroke="#8a3fc8" stroke-width="4" fill="none"/></svg></span>
  <span>Commissioning and instruction in charging technology</span>
</div>
<div class="feature" style="left:166px;top:2224px">
  <span class="feature-icon"><svg viewBox="0 0 52 52"><path d="M12,40 L36,16" stroke="#8a3fc8" stroke-width="6" stroke-linecap="round"/><path d="M12,12 L40,40" stroke="#e0259c" stroke-width="6" stroke-linecap="round"/></svg></span>
  <span>Annual technical maintenance according to DGUV3</span>
</div>
<div class="btn" style="left:502px;top:2330px;width:196px;height:50px;background:#6e56c9">CALL NOW</div>

<!-- Municipality -->
<h2 class="abs heading muni-title">As A Munincipality</h2>
<div class="abs bracket"></div>
<div class="abs photo" role="img" aria-label="Technician working on a car engine bay"></div>

<svg width="0" height="0" style="position:absolute">
  <symbol id="chev" viewBox="0 0 22 20"><path d="M2,2 L9,10 L2,18 M11,2 L18,10 L11,18" stroke="currentColor" stroke-width="3.5" fill="none"/></symbol>
</svg>

<ul class="check-list muni-list" style="color:var(--pink)">
  <li style="top:2752px"><svg><use href="#chev"/></svg><span style="color:var(--ink)">Conception of possible charging<br>infrastructures within your municipality</span></li>
  <li style="top:2809px"><svg><use href="#chev"/></svg><span style="color:var(--ink)">Planning and project management<br>including all official approval procedures<br>and application for subsidies</span></li>
  <li style="top:2888px"><svg><use href="#chev"/></svg><span style="color:var(--ink)">Professional installation and commissioning</span></li>
  <li style="top:2932px"><svg><use href="#chev"/></svg><span style="color:var(--ink)">Regular maintenance according to regulation</span></li>
  <li style="top:2970px"><svg><use href="#chev"/></svg><span style="color:var(--ink)">Repair and customer service</span></li>
  <li style="top:3010px"><svg><use href="#chev"/></svg><span style="color:var(--ink)">Direct billing with the user</span></li>
  <li style="top:3049px"><svg><use href="#chev"/></svg><span style="color:var(--ink)">Community participation in sales</span></li>
  <li style="top:3089px"><svg><use href="#chev"/></svg><span style="color:var(--ink)">Possibility of integrating bonus programs that<br>promote local retail</span></li>
</ul>
<div class="btn" style="left:630px;top:3174px;width:195px;height:50px">CALL NOW</div>

<!-- Business -->
<svg class="abs" style="left:0;top:3320px" width="1200" height="1160" viewBox="0 0 1200 1160" aria-hidden="true">
  <defs><linearGradient id="bizGrad" x1="0" y1="0" x2="0.6" y2="1"><stop offset="0" stop-color="#e0259c"/><stop offset="0.6" stop-color="#a83cc4"/><stop offset="1" stop-color="#7b4fd6"/></linearGradient></defs>
  <path d="M0,20 C300,70 600,-10 900,40 C1050,60 1150,50 1200,40 L1200,1160 L0,1160 Z" fill="url(#bizGrad)"/>
  <path d="M0,1168 L0,1160 C300,1090 800,1050 1200,1100 L1200,1168 Z" fill="#1a1d2e"/>
  <path d="M0,1146 C300,1076 800,1036 1200,1086" stroke="#fff" stroke-width="4" fill="none"/>
</svg>
<div class="abs footer-bg"></div>
<h2 class="abs heading biz-title">As A Business<br>Customer</h2>

<ul class="check-list biz-list" style="color:var(--white)">
  <li style="left:175px;top:3630px"><svg><use href="#chev"/></svg><div>Carrying out an individual needs analysis including determination of the requirements for:
    <ul class="biz-sub">
      <li>House and real estate management</li>
      <li>service and trading companies</li>
      <li>Hotel and accommodation establishments</li>
      <li>Parking and car park operators</li>
      <li>Tourism, sports and leisure facilities</li>
    </ul></div></li>
  <li style="left:175px;top:3905px"><svg><use href="#chev"/></svg><span>In existing buildings, integration of the charging infrastructure into the building system technology and, if necessary, adjustment of the grid connection</span></li>
  <li style="left:175px;top:4066px"><svg><use href="#chev"/></svg><span>Commissioning of the system including test and measurement reports</span></li>

  <li style="left:625px;top:3630px"><svg><use href="#chev"/></svg><span>Tourism, sports and leisure facilities</span></li>
  <li style="left:625px;top:3684px"><svg><use href="#chev"/></svg><span>Leasing or buying the hardware</span></li>
  <li style="left:625px;top:3737px"><svg><use href="#chev"/></svg><span>Standard-compliant installation of the charging infrastructure including breakthrough, fire protection and earthworks</span></li>
  <li style="left:625px;top:3858px"><svg><use href="#chev"/></svg><span>Exchange and repair service</span></li>
  <li style="left:625px;top:3907px"><svg><use href="#chev"/></svg><span>support with the monthly Usage billing and integration into your existing billing systems</span></li>
  <li style="left:625px;top:4013px"><svg><use href="#chev"/></svg><span>OR direct billing to users</span></li>
  <li style="left:625px;top:4068px"><svg><use href="#chev"/></svg><span>Wiederkehrende technische Prüfung der Anlage nach DGUV 3</span></li>
</ul>
<div class="btn" style="left:502px;top:4188px;width:196px;height:52px">CALL NOW</div>

<!-- Footer -->
<div class="abs brand" style="left:170px;top:4572px;font-size:40px"><span class="brand-dot" style="width:24px;height:24px"></span>vorn-werk.de</div>
<span class="social" style="left:174px" aria-label="Video channel"></span>
<span class="social" style="left:257px" aria-label="Social page"></span>
<span class="social" style="left:341px" aria-label="Photo feed"></span>

<div class="abs footer-head" style="left:565px;top:4478px">Links</div>
<ul class="abs footer-links">
  <li>Home</li><li>Solutions</li><li>Company</li><li>Services</li><li>Career</li><li>Contact</li>
</ul>

<div class="abs footer-head" style="left:790px;top:4478px">Contact</div>
<div class="contact-item" style="top:4560px">
  <span class="contact-icon"><svg width="18" height="22" viewBox="0 0 18 22"><path d="M9,21 C3,14 1,11 1,8 A8,8 0 0 1 17,8 C17,11 15,14 9,21 Z" fill="#fff"/><circle cx="9" cy="8" r="3" fill="#9a3fc4"/></svg></span>
  <span>123 ipsum dolor sit t,<br>consectetur vel<br>facilisis.</span>
</div>
<div class="contact-item" style="top:4656px">
  <span class="contact-icon"><svg width="20" height="14" viewBox="0 0 20 14"><rect x="1" y="1" width="18" height="12" rx="1" fill="#fff"/><path d="M1,1 L10,8 L19,1" stroke="#9a3fc4" stroke-width="1.6" fill="none"/></svg></span>
  <span>info@companyname.com</span>
</div>
<div class="contact-item" style="top:4710px">
  <span class="contact-icon"><svg width="18" height="18" viewBox="0 0 18 18"><path d="M4,1 L7,5 L5,7 C6,10 8,12 11,13 L13,11 L17,14 L15,17 C8,17 1,10 1,3 Z" fill="#fff"/></svg></span>
  <span>+1234-5678-921</span>
</div>

<div class="abs footer-rule"></div>
<p class="abs copyright">Copyright © 2022 vorn-werk GmbH. All rights reserved.</p>

</body>
</html>
```